Flyer-Design für Personalvermittlung
Zielgruppe
Wir machen Personalvermittlung (www.kraftwendel.de), Unternehmen, die einen eigenen Kunden haben sowie Unternehmen, die Kundenservice als Dienstleistung anbieten. DIe Zielgruppe sind Personalentscheider, Recruiter, HR-Direktoren, Kundenservicecenter-Leiter, Geschäftsführer). Weiterhin zählt zur Zielgruppe jeder wechselwillige Kandidat, der sich bei kraftwendel registrieren kann.
Aufgabenstellung
Ich hätte gerne ein zweiseitiges Flyerformat, was über Hostessen verteilbar ist, also nicht größer als A5. Inhalte können gerne aus der Homepage entnommen werden. Weiterhin in der Anlage ein Teaser, den wir Unternehmen zur Verfügung stellen. Vorderseite für Unternehmen, Rückseite für Kandidaten. Kernige Aussagen, wenig Text.

```html
<!DOCTYPE html>
<html lang="de">
<head>
<meta charset="utf-8">
<title>Kraftwendel – Chancengeber</title>
<link rel="stylesheet" href="https://fonts.googleapis.com/css2?family=Roboto+Condensed:wght@700&family=Roboto:wght@500&display=swap">
<style>
  :root {
    --navy: #1f2738;
    --teal-strong: #0ba396;
    --teal-soft: #74c5b2;
    --white: #ffffff;
    --wall-light: #e4e4e4;
    --wall-dark: #c9c9c9;
    --shirt: #8d9bbf;
  }
  * { margin: 0; padding: 0; box-sizing: border-box; }
  html, body { width: 1200px; height: 846px; overflow: hidden; }
  .flyer {
    position: relative;
    width: 1200px;
    height: 846px;
    overflow: hidden;
    font-family: "Roboto Condensed", "Arial Narrow", sans-serif;
    color: var(--navy);
  }
  .wall-backdrop {
    position: absolute; inset: 0;
    background: radial-gradient(ellipse at 50% 40%, var(--wall-light) 0%, var(--wall-dark) 100%);
  }
  .search-bar {
    position: absolute; left: 108px; top: 126px;
    width: 829px; height: 124px;
    background: rgba(255,255,255,0.93);
    display: flex; align-items: center; justify-content: center;
  }
  .search-term {
    font-size: 64px; font-weight: 700; letter-spacing: 1px;
    padding-left: 70px;
  }
  .search-button {
    position: absolute; left: 937px; top: 126px;
    width: 157px; height: 124px;
    background: var(--teal-strong);
    display: flex; align-items: center; justify-content: center;
  }
  .headline {
    position: absolute; left: 200px; top: 278px; width: 772px;
    text-align: center;
    font-size: 48px; font-weight: 700; line-height: 54px;
    letter-spacing: 0.5px;
  }
  .signup-panel {
    position: absolute; left: 0; top: 489px;
    width: 494px; height: 242px;
    background: var(--teal-soft);
    padding: 30px 0 0 37px;
    font-family: "Roboto", Arial, sans-serif;
    font-weight: 500; font-size: 35px; line-height: 47px;
  }
  .signup-panel .lead { color: var(--white); }
  .signup-panel .web { color: var(--navy); }
  .consultant-photo {
    position: absolute; left: 360px; top: 426px;
    width: 310px; height: 363px;
    background: linear-gradient(180deg, #d9c6a8 0%, #b9c0d6 38%, var(--shirt) 100%);
    border-radius: 150px 150px 0 0;
  }
  .brand-mark {
    position: absolute; left: 888px; top: 482px;
    width: 236px; height: 236px;
    border-radius: 50%;
    background: var(--navy);
  }
  .brand-name {
    position: absolute; left: 856px; top: 728px; width: 300px;
    text-align: center;
    font-size: 34px; font-weight: 700;
  }
  .contact-strip {
    position: absolute; left: 0; top: 789px;
    width: 1200px; height: 57px;
    background: var(--navy);
    color: var(--white);
    font-family: "Roboto", Arial, sans-serif;
    font-weight: 500; font-size: 18px;
    display: flex; align-items: center; justify-content: center;
    gap: 12px; letter-spacing: 0.3px;
  }
</style>
</head>
<body>
<main class="flyer">
  <div class="wall-backdrop" role="img" aria-label="Hintergrund: weiß gestrichene Ziegelwand"></div>

  <div class="search-bar"><span class="search-term">CHANCENGEBER</span></div>
  <div class="search-button">
    <svg width="66" height="66" viewBox="0 0 66 66" aria-hidden="true">
      <circle cx="26" cy="26" r="17" fill="none" stroke="#ffffff" stroke-width="7"/>
      <line x1="38" y1="38" x2="58" y2="58" stroke="#ffffff" stroke-width="9" stroke-linecap="round"/>
    </svg>
  </div>

  <h1 class="headline">WIR FINDEN DEN RICHTIGEN JOB<br>FÜR IHRE KARRIERE.</h1>

  <div class="signup-panel">
    <p class="lead">Jetzt anmelden &amp;<br>neuen Job finden</p>
    <p class="web">www.kraftwendel.de</p>
  </div>

  <div class="consultant-photo" role="img" aria-label="Foto: lächelnde Kundenberaterin mit Headset in blauer Bluse"></div>

  <div class="brand-mark" aria-hidden="true"></div>
  <div class="brand-name">KRAFTWENDEL</div>

  <footer class="contact-strip">
    <span>KRAFTWENDEL</span><span>·</span>
    <span>KÖRNERSTRASSE 9</span><span>·</span>
    <span>10785 BERLIN</span><span>·</span>
    <span>+49 [0] 30 512 336 780</span><span>·</span>
    <span>INFO@KRAFTWENDEL.DE</span>
  </footer>
</main>
</body>
</html>
```